Veterinary Power Point Template/Master

Dear Creatives,
we would need a Power Point Template that can be used for internal and external presentations. It'll mostly be needed to create B2B presentations at congresses or seminars, at which our vets attend as podium guests and lecturers.

What is important?
We see ourselves as highly professional, clean and innovative. One of our greatest mission is to build our work on latest medical research and the latest technology within veterinary medicine.
Therefore, our design should represent exactly this and look modern, professional and clinical.

Which slides do we need? What should they include?
- title
- section slides
- agenda
- Team slides to introduce our personell
- classic title & content
- slides to include different media and text options
- page numbers
- date
- our logo
- icons (if possible)

Unfortunately, we do not have an english version of our website yet, but feel free to browse through it to get a feeling for our appearance and values: https://www.tierpraxamo.at

We will also attach our little brand booklet as a guidance for you. BUT feel free to think out of the box and create a beautiful PPT design which is fun to watch.

Thrilled to see your great work already!

Target Market(s)

Austria

Industry/Entity Type

veterinary medicine

Font styles to use
Sans Serif
Other font styles liked:
• please only use Roboto font

Requirements
Must have
• items described in the creative brief
Nice to have
• animations and fancy transitions
Should not have
• Comic Sans or classic PPT Preset Designs

```html
<!DOCTYPE html>
<html lang="en">
<head>
<meta charset="utf-8">
<title>Vetalis – Presentation Template</title>
<link href="https://fonts.googleapis.com/css2?family=Baloo+2:wght@600;700;800&family=Roboto:wght@300;400;500&display=swap" rel="stylesheet">
<style>
  :root{
    --navy:#263a4f;
    --navy-dark:#1f3042;
    --gold:#c99a0a;
    --gold-soft:#d9ae2a;
    --page:#4a4a4a;
    --white:#ffffff;
    --text:#3b3b3b;
    --muted:#666b70;
    --band:#dde0e4;
  }
  *{margin:0;padding:0;box-sizing:border-box;}
  html,body{width:1200px;height:4087px;overflow:hidden;background:var(--page);}
  body{position:relative;font-family:"Roboto",sans-serif;color:var(--text);}
  .slide{position:absolute;left:24px;width:1152px;height:648px;background:var(--white);overflow:hidden;}
  .heading{font-family:"Baloo 2",sans-serif;font-weight:700;color:#1e1e1e;}
  .accent{color:var(--gold);}
  .slide-title{position:absolute;left:48px;top:22px;font-size:38px;line-height:1.2;}
  .title-rule{position:absolute;left:41px;top:78px;width:855px;height:3px;background:var(--gold);}
  .brand{position:absolute;left:908px;top:12px;width:230px;height:66px;}
  .brand-dot{position:absolute;left:0;top:1px;width:62px;height:62px;border-radius:50%;background:var(--gold);border:4px solid var(--navy);}
  .brand-name{position:absolute;left:74px;top:6px;font-family:"Baloo 2",sans-serif;font-weight:700;font-size:23px;color:var(--navy);line-height:1.2;}
  .brand-tag{position:absolute;left:74px;top:36px;font-family:"Baloo 2",sans-serif;font-weight:600;font-size:9.5px;color:var(--gold);}
  .footer{position:absolute;right:51px;top:605px;font-size:11.5px;font-weight:500;color:#222;}
  .footer span{color:var(--gold);}
  .photo{position:absolute;}
  /* title slide */
  .cover{background:linear-gradient(135deg,#2d4358 0%,var(--navy) 55%,var(--navy-dark) 100%);}
  .cover-photo{left:0;top:0;width:1152px;height:648px;background:linear-gradient(90deg,rgba(255,255,255,0) 0%,rgba(255,255,255,.05) 40%,rgba(255,255,255,.08) 60%,rgba(255,255,255,0) 100%);}
  .cover-badge{position:absolute;left:465px;top:148px;width:222px;height:222px;border-radius:50%;background:var(--gold);border:12px solid var(--white);box-shadow:0 0 0 6px var(--gold);}
  .cover-name{position:absolute;left:0;width:100%;top:388px;text-align:center;font-family:"Baloo 2",sans-serif;font-weight:700;font-size:72px;line-height:1;color:var(--white);}
  .cover-tag{position:absolute;left:0;width:100%;top:466px;text-align:center;font-family:"Baloo 2",sans-serif;font-weight:700;font-size:31px;color:var(--gold);}
  /* agenda */
  .agenda-item{position:absolute;height:80px;}
  .agenda-num{position:absolute;left:0;top:0;width:80px;height:80px;border-radius:50%;background:var(--white);border:2px solid #e3c66e;box-shadow:0 3px 10px rgba(0,0,0,.18);display:flex;align-items:center;justify-content:center;font-family:"Baloo 2",sans-serif;font-weight:700;font-size:28px;color:var(--navy);}
  .agenda-label{position:absolute;left:100px;top:20px;white-space:nowrap;font-size:26px;}
  /* text blocks */
  .text-card{position:absolute;left:487px;top:162px;width:616px;height:406px;background:var(--white);border:2px solid var(--gold-soft);border-radius:12px;box-shadow:0 4px 14px rgba(0,0,0,.12);padding:20px 24px;}
  .body-text{font-size:13.4px;line-height:23px;color:var(--text);}
  .body-text p+p{margin-top:9px;}
  .about-text{position:absolute;left:76px;top:150px;width:505px;font-size:14.6px;line-height:24.5px;}
  /* team */
  .member{position:absolute;width:220px;margin-left:-110px;text-align:center;}
  .member-photo{width:88px;height:88px;border-radius:50%;margin:0 auto;background:linear-gradient(180deg,#f3f3f3 0%,#f3f3f3 48%,#3a3d42 48%,#2b2e33 100%);box-shadow:inset 0 0 0 1px #e6e6e6;}
  .member-name{margin-top:3px;font-family:"Baloo 2",sans-serif;font-weight:700;font-size:15.5px;line-height:1.2;color:var(--navy);white-space:nowrap;}
  .member-role{font-size:10.5px;line-height:15px;color:var(--muted);padding:0 8px;}
  /* contact */
  .contact-title{position:absolute;left:636px;top:206px;font-size:38px;}
  .contact-row{position:absolute;left:632px;display:flex;align-items:center;}
  .contact-icon{width:72px;height:72px;border-radius:50%;background:var(--navy);border:3px solid var(--white);box-shadow:0 0 0 3px var(--gold);display:flex;align-items:center;justify-content:center;flex-shrink:0;}
  .contact-text{margin-left:18px;font-size:18.5px;line-height:27px;color:#2a2a2a;font-weight:300;}
</style>
</head>
<body>

<!-- Title slide -->
<section class="slide cover" style="top:27px;">
  <div class="photo cover-photo" role="img" aria-label="Faded photo of a veterinarian examining a pet in a clinic"></div>
  <svg width="1152" height="648" style="position:absolute;left:0;top:0;">
    <polygon points="0,112 0,148 88,0 52,0" fill="var(--gold)"/>
    <polygon points="0,184 0,224 132,0 92,0" fill="var(--gold)"/>
    <polygon points="900,648 940,648 1152,292 1152,228" fill="var(--gold)"/>
    <polygon points="980,648 1022,648 1152,430 1152,362" fill="var(--gold)"/>
  </svg>
  <div class="cover-badge"></div>
  <div class="cover-name">Vetalis</div>
  <div class="cover-tag">Fachklinik für Kleintiere</div>
</section>

<!-- Agenda -->
<section class="slide" style="top:705px;">
  <svg width="1152" height="648" style="position:absolute;left:0;top:0;">
    <polygon points="0,320 0,390 180,648 250,648" fill="var(--band)"/>
  </svg>
  <div class="photo" role="img" aria-label="Photo of a bright veterinary examination room with steel table and lamp" style="left:56px;top:116px;width:675px;height:501px;background:linear-gradient(180deg,#f4f5f6 0%,#e9ebed 50%,#b9bec3 68%,#dfe2e5 100%);clip-path:polygon(0 0,525px 0,675px 501px,0 501px);"></div>
  <svg width="1152" height="648" style="position:absolute;left:0;top:0;">
    <line x1="581" y1="116" x2="733" y2="617" stroke="var(--gold)" stroke-width="9"/>
  </svg>
  <h1 class="heading slide-title">Agenda</h1>
  <div class="title-rule"></div>
  <div class="brand"><div class="brand-dot"></div><div class="brand-name">Vetalis</div><div class="brand-tag">Fachklinik für Kleintiere</div></div>

  <div class="agenda-item" style="left:552px;top:147px;"><div class="agenda-num">03</div><div class="heading agenda-label">Welcome to <span class="accent">Vetalis</span></div></div>
  <div class="agenda-item" style="left:585px;top:266px;"><div class="agenda-num">04</div><div class="heading agenda-label">About To <span class="accent">Vetalis</span></div></div>
  <div class="agenda-item" style="left:631px;top:379px;"><div class="agenda-num">05</div><div class="heading agenda-label">Our <span class="accent">Team</span></div></div>
  <div class="agenda-item" style="left:668px;top:498px;"><div class="agenda-num">06</div><div class="heading agenda-label">Contact <span class="accent">Us</span></div></div>

  <div class="footer">07/09/2023 - <span>Page - 02</span></div>
</section>

<!-- Welcome -->
<section class="slide" style="top:1384px;">
  <h1 class="heading slide-title">Welcome to <span class="accent">Vetalis</span></h1>
  <div class="title-rule"></div>
  <div class="brand"><div class="brand-dot"></div><div class="brand-name">Vetalis</div><div class="brand-tag">Fachklinik für Kleintiere</div></div>
  <div class="photo" role="img" aria-label="Architectural rendering of the modern clinic building with wooden slat facade" style="left:41px;top:130px;width:626px;height:470px;border-radius:8px;background:linear-gradient(180deg,#e4eaef 0%,#eef1f3 30%,#b07a4e 48%,#8a5a36 66%,#c7c9cb 82%,#aab0a4 100%);"></div>
  <div class="text-card body-text">
    <p>Your favourite four-legged friend deserves the best treatment? We think so too! That's why we are opening one of the largest and most modern veterinary clinics in Europe in the south of Vienna from autumn 2022. At the Vetalis, the best care for your four-legged friend is our top priority. All of our leading vets are know European specialists in their fields. this is unique in the private sector. On top of we will work in a state-of-the-art building with modern medical equipment.</p>
    <p>Modern medicine involves knowledge that is growing almost daily and permanent progress. This also applies to veterinary medicine, whose diagnostic and therapeutic methods are becoming increasingly complex. For this reason, our senior veterinarians have completed many years of training as specialists according to the guidelines of various European or American colleges. The diplomas they have earned as a result are among the most demanding in veterinary medicine worldwide. Today, advanced veterinary medicine is inconceivable without modern medical technology. That is why we have everything under one roof. We combine specialist expertise with state-of-the-art medical technology.</p>
  </div>
  <div class="footer">07/09/2023 - <span>Page - 03</span></div>
</section>

<!-- About -->
<section class="slide" style="top:2062px;">
  <svg width="1152" height="648" style="position:absolute;left:0;top:0;">
    <polygon points="0,300 0,380 230,648 320,648" fill="var(--band)"/>
  </svg>
  <h1 class="heading slide-title">About To <span class="accent">Vetalis</span></h1>
  <div class="title-rule"></div>
  <div class="brand"><div class="brand-dot"></div><div class="brand-name">Vetalis</div><div class="brand-tag">Fachklinik für Kleintiere</div></div>
  <div class="about-text body-text">
    <p>Your favourite four-legged friend deserves the best treatment? We think so too! That's why we are opening one of the largest and most modern veterinary clinics in Europe in the south of Vienna from autumn 2022. At the Vetalis, the best care for your four-legged friend is our top priority. All of our leading vets are know European specialists in their fields. this is unique in the private sector. On top of we will work in a state-of-the-art building with modern medical equipment.</p>
    <p>The Vetalis is one of the largest and most modern private veterinary clinics in Europe, located directly in the south of Vienna. For us, providing the best veterinary care for your four-legged friend is our top priority. In addition to the outstanding technical expertise of our specialists, we offer state-of-the-art diagnostic and therapeutic options. The vet clinic is staffed around the clock for emergencies.</p>
  </div>
  <div class="photo" role="img" aria-label="Photo of a veterinarian examining a ginger cat" style="left:640px;top:121px;width:444px;height:444px;border-radius:50%;border:6px solid var(--gold);background:linear-gradient(160deg,#f4f6f8 0%,#eef0f2 35%,#e2b27c 60%,#d89a5a 80%,#f1ede8 100%);"></div>
  <div class="photo" role="img" aria-label="Photo of a vet listening to a cat with a stethoscope" style="left:575px;top:279px;width:254px;height:254px;border-radius:50%;border:5px solid var(--white);background:linear-gradient(160deg,#f6f6f6 0%,#ece7e1 40%,#d8a06a 70%,#efe6dc 100%);"></div>
  <div class="photo" role="img" aria-label="Photo of a small dog and a grey cat" style="left:0;top:470px;width:62px;height:150px;background:linear-gradient(180deg,#a7835f 0%,#c8b196 48%,#9b9ea2 52%,#8d9094 100%);border-radius:0 30px 30px 0;"></div>
  <div class="photo" role="img" aria-label="Photo of a cat and a golden retriever" style="left:1080px;top:425px;width:72px;height:190px;background:linear-gradient(180deg,#dcae7a 0%,#e8c495 50%,#d7a86e 52%,#caa06a 100%);border-radius:36px 0 0 36px;"></div>
  <div class="footer">07/09/2023 - <span>Page - 04</span></div>
</section>

<!-- Team -->
<section class="slide" style="top:2741px;">
  <svg width="1152" height="648" style="position:absolute;left:0;top:0;">
    <polygon points="0,330 0,400 200,648 280,648" fill="var(--band)"/>
  </svg>
  <h1 class="heading slide-title">Our <span class="accent">Team</span></h1>
  <div class="title-rule"></div>
  <div class="brand"><div class="brand-dot"></div><div class="brand-name">Vetalis</div><div class="brand-tag">Fachklinik für Kleintiere</div></div>

  <div class="member" style="left:133px;top:116px;"><div class="member-photo" role="img" aria-label="Portrait photo of team member"></div><div class="member-name">Dr. Lukas Brenner</div><div class="member-role">Diplomate ECVS, specialist in surgery, clinic manager, managing director</div></div>
  <div class="member" style="left:354px;top:116px;"><div class="member-photo" role="img" aria-label="Portrait photo of team member"></div><div class="member-name">Dr. Florian Weiss</div><div class="member-role">Diplomate ECVIM-CA, specialist in internal medicine, clinic manager</div></div>
  <div class="member" style="left:574px;top:116px;"><div class="member-photo" role="img" aria-label="Portrait photo of team member"></div><div class="member-name">Dr. Tobias Kern</div><div class="member-role">Specialist in internal medicine, clinic manager</div></div>
  <div class="member" style="left:778px;top:116px;"><div class="member-photo" role="img" aria-label="Portrait photo of team member"></div><div class="member-name">Dr. Jonas Reiter</div><div class="member-role">Diplomate ACVECC, Specialist in Emergency and Critical Care Medicine, Head of Clinic</div></div>
  <div class="member" style="left:1011px;top:116px;"><div class="member-photo" role="img" aria-label="Portrait photo of team member"></div><div class="member-name">Dr. Ingrid Marie Falk</div><div class="member-role">Surgery, emergency and intensive care medicine</div></div>

  <div class="member" style="left:133px;top:294px;"><div class="member-photo" role="img" aria-label="Portrait photo of team member"></div><div class="member-name">Mag. Veronika Stadlmayr-Ortner</div><div class="member-role">Neurologie, Innere Medizin, Notfall- und Intensivmedizin</div></div>
  <div class="member" style="left:354px;top:294px;"><div class="member-photo" role="img" aria-label="Portrait photo of team member"></div><div class="member-name">Mag. Petra Kainz</div><div class="member-role">Innere Medizin, Notfall- und Intensivmedizin</div></div>
  <div class="member" style="left:574px;top:294px;"><div class="member-photo" role="img" aria-label="Portrait photo of team member"></div><div class="member-name">VMDr. Lenka Novakova, PhD</div><div class="member-role">Innere Medizin, Notfall-und Intensivmedizin</div></div>
  <div class="member" style="left:778px;top:294px;"><div class="member-photo" role="img" aria-label="Portrait photo of team member"></div><div class="member-name">Mag. Ravi Hollerer</div><div class="member-role">Notfall- und Intensivmedizin</div></div>
  <div class="member" style="left:1011px;top:294px;"><div class="member-photo" role="img" aria-label="Portrait photo of team member"></div><div class="member-name">Dr. Sabine Moser</div><div class="member-role">FTA für Kleintiermedizin, Spezialistin für Chirurgie</div></div>

  <div class="member" style="left:133px;top:461px;"><div class="member-photo" role="img" aria-label="Portrait photo of team member"></div><div class="member-name">Dr. med. vet. Miriam Eder</div><div class="member-role">Diplomate ECAR, Spezialistin für Reproduktionsmedizin</div></div>
  <div class="member" style="left:354px;top:461px;"><div class="member-photo" role="img" aria-label="Portrait photo of team member"></div><div class="member-name">Mag. Eva Hruska</div><div class="member-role">Dermatologie</div></div>
  <div class="member" style="left:574px;top:461px;"><div class="member-photo" role="img" aria-label="Portrait photo of team member"></div><div class="member-name">Mag. Julia Prammer</div><div class="member-role">Chirurgie, Notfall- und Intensivmedizin</div></div>
  <div class="member" style="left:778px;top:461px;"><div class="member-photo" role="img" aria-label="Portrait photo of team member"></div><div class="member-name">Mag. Theresa Gruber</div><div class="member-role">Certified Canine Rehabilitation Practioner (CCRP), Spezialistin für Physiotherapie</div></div>

  <div class="footer">07/09/2023 - <span>Page - 05</span></div>
</section>

<!-- Contact -->
<section class="slide" style="top:3420px;">
  <div class="photo" role="img" aria-label="Photo of a veterinarian holding a spaniel puppy and a ginger kitten" style="left:0;top:0;width:900px;height:648px;background:linear-gradient(180deg,#f1f3f5 0%,#e6eaed 35%,#e5c49c 60%,#dda46a 80%,#e9e2da 100%);"></div>
  <svg width="1152" height="648" style="position:absolute;left:0;top:0;">
    <path d="M683,0 C640,70 590,150 600,240 C610,330 700,380 760,450 C810,510 850,580 865,648 L1152,648 L1152,0 Z" fill="var(--white)"/>
  </svg>
  <div class="brand"><div class="brand-dot"></div><div class="brand-name">Vetalis</div><div class="brand-tag">Fachklinik für Kleintiere</div></div>
  <h1 class="heading contact-title">Contact <span class="accent">Us</span></h1>

  <div class="contact-row" style="top:266px;">
    <div class="contact-icon">
      <svg width="26" height="32" viewBox="0 0 24 30"><path d="M12 0C5.9 0 1 4.9 1 11c0 8.2 11 19 11 19s11-10.8 11-19C23 4.9 18.1 0 12 0zm0 15.5a4.5 4.5 0 1 1 0-9 4.5 4.5 0 0 1 0 9z" fill="var(--gold)"/></svg>
    </div>
    <div class="contact-text">Vetalis GmbH &amp; Co KG<br>Brunnenfeldgasse 118B<br>1230 Vienna</div>
  </div>
  <div class="contact-row" style="top:361px;">
    <div class="contact-icon">
      <svg width="28" height="28" viewBox="0 0 24 24"><path d="M6.6 10.8a15.2 15.2 0 0 0 6.6 6.6l2.2-2.2c.3-.3.7-.4 1-.2 1.1.4 2.3.6 3.6.6.6 0 1 .4 1 1V20c0 .6-.4 1-1 1C10.6 21 3 13.4 3 4c0-.6.4-1 1-1h3.5c.6 0 1 .4 1 1 0 1.3.2 2.5.6 3.6.1.3 0 .7-.2 1l-2.3 2.2z" fill="var(--gold)"/></svg>
    </div>
    <div class="contact-text">+43(0)1 58210</div>
  </div>
  <div class="contact-row" style="top:459px;">
    <div class="contact-icon">
      <svg width="30" height="22" viewBox="0 0 30 22"><rect x="0" y="0" width="30" height="22" rx="3" fill="var(--gold)"/><path d="M1.5 2 L15 12 L28.5 2" fill="none" stroke="var(--navy)" stroke-width="2.4"/></svg>
    </div>
    <div class="contact-text">info@vetalis.at</div>
  </div>

  <div class="photo" role="img" aria-label="Photo of a husky and a grey cat" style="left:900px;top:420px;width:220px;height:172px;border-radius:12px;background:linear-gradient(180deg,#eceef0 0%,#c9ccd0 45%,#8f949a 100%);"></div>

  <div class="footer">07/09/2023 - <span>Page - 06</span></div>
</section>

</body>
</html>
```